Letterhead for 3 attorney Workers' Comp law firm

We are a 3 attorney law office. We specialize in Workers' Compensation. Our office represents workers who are injured on the job, and the estates of workers who are killed one the job.
When we started our office, we created our own letterhead & have been using it for years. We've just recently hired the 3rd attorney, and were going to just add his name to the letterhead, but have decided we wanted to get a professionally designed letterhead and business cards at this point.
We want something that looks clean and professional. It must look good in black and white because we often make multiple copies of our documents. We're hoping for a design that resonates confidence, reliability and experience.
The design must include the firm name: Thornbury & Calder, PLLC. We would like the PLLC to be small compared to the Thornbury & Calder graphic. We also want to incorporate the attorney names: Ivar Thornbury, Delia Calder, and Glen Rutledge. Our current letterhead has our contact info in the footer at the bottom of the page. We like that design, but are open to the idea of having it at the top. We'll leave that at the discretion of the designer. Our contact info is as follows: 482 S. Harrow Avenue, Suite 310 Bellingham, WA 98417 Phone: 360-555-2917, Fax: 360-555-4068, and our website: www.thornburycalder.example
Target Market(s)
Clients, courts, other legal offices, doctors offices. These are the people who see our letterhead most frequently. It's not so much for marketing purposes, mainly so that we have a professional image when sending out documents.
Industry/Entity Type
Law Firm
Contact Information for Business Card
On the back of the business card: it can be designed, or be a template for filling in appointment reminder information (i.e. date, time, etc)
Colors
Designer to choose colors to be used in the design.
Requirements
Must have
- Must have our firm name at the top.
- Must include the attorney names.
- Must have all of our contact information (can be at top or bottom - whatever looks best with the design)
Nice to have
- A strong, confident design
Should not have
- We don't want the design to be playful, cartoony or busy.

```html
<!DOCTYPE html>
<html lang="en">
<head>
<meta charset="utf-8">
<title>Thornbury &amp; Calder, PLLC — Letterhead</title>
<link rel="stylesheet" href="https://fonts.googleapis.com/css2?family=Libre+Baskerville:wght@700&family=Roboto+Condensed:wght@700&family=Roboto:wght@400&family=Lato:wght@400;700&display=swap">
<style>
  :root {
    --navy: #00355f;
    --backdrop: #c9c9c9;
    --paper: #e7e7e7;
    --ink: #333333;
    --ink-soft: #555555;
  }
  * { margin: 0; padding: 0; box-sizing: border-box; }
  html, body {
    width: 987px;
    height: 1200px;
    overflow: hidden;
    background: var(--backdrop);
  }
  .letterhead {
    position: absolute;
    left: 83px;
    top: 20px;
    width: 820px;
    height: 1160px;
    background: var(--paper);
  }
  .firm-name {
    position: absolute;
    left: 56px;
    top: 70px;
    font-family: "Libre Baskerville", "Times New Roman", serif;
    font-weight: 700;
    font-size: 24px;
    letter-spacing: 0.2px;
    color: var(--navy);
    text-transform: uppercase;
    white-space: nowrap;
  }
  .firm-name .entity {
    font-size: 15px;
    letter-spacing: 1px;
  }
  .attorneys {
    position: absolute;
    left: 57px;
    top: 114px;
    list-style: none;
    font-family: "Roboto Condensed", "Arial Narrow", sans-serif;
    font-weight: 700;
    font-size: 14.5px;
    line-height: 18.5px;
    color: var(--navy);
    text-transform: uppercase;
  }
  .contact {
    position: absolute;
    right: 57px;
    top: 90px;
    font-family: "Roboto", Arial, sans-serif;
    font-size: 11.5px;
    line-height: 14.8px;
    color: var(--ink-soft);
    text-align: right;
    font-style: normal;
  }
  .contact .line { display: flex; justify-content: flex-end; align-items: center; gap: 6px; }
  .contact svg { width: 11px; height: 11px; fill: var(--navy); }
  .letter {
    position: absolute;
    left: 58px;
    top: 370px;
    width: 706px;
    font-family: "Lato", Arial, sans-serif;
    font-size: 14.2px;
    line-height: 18.2px;
    color: var(--ink);
  }
  .letter .salutation { margin-bottom: 29px; }
  .letter p.body { margin-bottom: 18px; text-align: justify; }
  .letter .signoff { margin-top: 36px; line-height: 20px; }
  .letter .signoff strong { font-weight: 700; display: block; }
  .footer-band {
    position: absolute;
    left: 0;
    bottom: 0;
    width: 100%;
    height: 9px;
    background: var(--navy);
  }
</style>
</head>
<body>
  <main class="letterhead">
    <h1 class="firm-name">Thornbury &amp; Calder<span class="entity">, PLLC</span></h1>

    <ul class="attorneys">
      <li>Ivar Thornbury</li>
      <li>Delia Calder</li>
      <li>Glen Rutledge</li>
    </ul>

    <address class="contact">
      <div class="line">482 S. Harrow Avenue</div>
      <div class="line">Suite 310 Bellingham, WA 98417</div>
      <div class="line">360-555-2917
        <svg viewBox="0 0 24 24" aria-hidden="true"><path d="M6.6 10.8a15.2 15.2 0 0 0 6.6 6.6l2.2-2.2a1 1 0 0 1 1-.25 11.4 11.4 0 0 0 3.6.57 1 1 0 0 1 1 1V20a1 1 0 0 1-1 1A17 17 0 0 1 3 4a1 1 0 0 1 1-1h3.5a1 1 0 0 1 1 1c0 1.25.2 2.45.57 3.57a1 1 0 0 1-.25 1z"/></svg>
      </div>
      <div class="line">360-555-4068
        <svg viewBox="0 0 24 24" aria-hidden="true"><path d="M7 2h10v5H7z"/><path d="M4 8h16a2 2 0 0 1 2 2v7h-3v5H5v-5H2v-7a2 2 0 0 1 2-2zm3 8v4h10v-4z"/></svg>
      </div>
      <div class="line">www.thornburycalder.example
        <svg viewBox="0 0 24 24" aria-hidden="true"><path d="M12 2a10 10 0 1 0 0 20 10 10 0 0 0 0-20zm-1 17.9A8 8 0 0 1 4.1 11H7l2 2v2l2 2zm6.9-2.5A2 2 0 0 0 16 16h-1v-3a1 1 0 0 0-1-1H8v-2h2a1 1 0 0 0 1-1V7h2a2 2 0 0 0 2-2v-.4a8 8 0 0 1 2.9 12.8z"/></svg>
      </div>
    </address>

    <article class="letter">
      <p class="salutation">Dear Mr. Hale,</p>
      <p class="body">Lorem ipsum dolor sit amet, consectetur adipiscing elit. Donec orci purus, luctus vitae dignissim eu, iaculis sed purus. Vivamus faucibus, ipsum nec aliquet viverra, leo mauris condimentum ligula, sit amet sagittis enim ligula quis arcu. Nam egestas tortor id nisi porttitor mattis. In tortor ante, ultricies in suscipit a, tempus non massa. Vivamus et auctor mi.</p>
      <p class="body">Fusce vel massa nulla. Phasellus nec eros mauris, et scelerisque orci. Donec malesuada orci vitae nulla accumsan porta a id massa. Quisque accumsan iaculis magna sit amet fringilla. Maecenas consequat, magna eget tincidunt semper, odio nibh rutrum mi, id feugiat ante nisi eu risus. Vestibulum nunc orci, rhoncus a placerat in, ultricies in mi. Cras mattis varius eros, vel fringilla nisi suscipit eget.</p>
      <p class="body">Quisque scelerisque sagittis nulla at porttitor. Mauris a justo et tellus interdum tristique. Sed id augue vitae urna euismod commodo aliquet a quam. Pellentesque arcu velit, cursus et malesuada ut, consequat et diam. Nullam erat sem, rhoncus id ullamcorper vitae, rhoncus et arcu. In ultricies ultricies nulla, ut rutrum nisi iaculis at. Donec eu magna a metus ornare faucibus.</p>
      <p class="body">Fusce aliquet faucibus ultricies. Morbi semper, est id tincidunt gravida, sem arcu adipiscing lacus, ac bibendum nulla leo eu purus. Quisque nec diam sed risus consectetur a ccumsan quis quis nibh. Vestibulum id purus lore</p>
      <p class="signoff"><strong>Alan Reyes</strong>Co-Founder &amp; CEO</p>
    </article>

    <div class="footer-band"></div>
  </main>
</body>
</html>
```